Clean professional design needed for landscape property business

We need a logo for a new lawncare, landscaping , property maintenance business called Fernway Grove.
Our services include lawn mowing, garden maintenance, clean ups and some property maintenance.
We want a double sided business card that is clean and very professional using the colour scheme from our logo which is provided.
the business card should have impact as we will use these to drop into people's letterboxes as a marketing drop.
Initially we want to see what you come up with so there is a very wide scope here to work with.

Project Deadline Extended
Reason: we feel our original deadline was too short. we have extended to give more time for quality submissions.

Target Market(s)

High end property owners who don't wish to do there own gardneing or property maintenance

Industry/Entity Type

Business

Contact Information for Business Card

Name
Postion/ Title
Phone number
mobile
web address
physical address

services offered

Font styles to use
Sans Serif

Requirements
Must have
• curved edges preferrred
Nice to have
• We like the idea of the logo being embossed or etched into the card so it looks like it is below the surface of the card
Should not have
• No stock images or characters.

```html
<!DOCTYPE html>
<html lang="en">
<head>
<meta charset="utf-8">
<title>Fernway Grove – Business Card</title>
<link rel="stylesheet" href="https://fonts.googleapis.com/css2?family=Open+Sans:wght@400;600;700&display=swap">
<style>
  :root {
    --page-bg: #ecebe7;
    --leaf-green: #7cc11a;
    --leaf-green-dark: #5f9e0d;
    --leaf-green-light: #8fd12a;
    --card-white: #ffffff;
    --card-grey: #f1f1f1;
    --ink: #4a4a4a;
    --ink-dark: #333333;
    --on-green: #ffffff;
  }
  * { box-sizing: border-box; margin: 0; padding: 0; }
  html, body {
    width: 1200px; height: 843px; overflow: hidden;
    background: var(--page-bg);
    font-family: "Open Sans", Arial, sans-serif;
  }
  .stage {
    position: relative; width: 1200px; height: 843px;
  }
  .card {
    position: absolute;
    width: 525px; height: 300px;
    border-radius: 22px;
    overflow: hidden;
    box-shadow: 0 10px 28px rgba(0,0,0,0.18);
  }

  /* Back side */
  .card--back {
    left: 50px; top: 150px;
    background: linear-gradient(135deg, var(--leaf-green-light), var(--leaf-green) 55%, var(--leaf-green-dark));
    color: var(--on-green);
    display: flex; flex-direction: column; align-items: center; justify-content: center;
    text-align: center;
  }
  .back-brand {
    display: flex; align-items: center; gap: 12px;
    margin-bottom: 34px;
  }
  .back-brand__name {
    font-size: 40px; font-weight: 700; letter-spacing: -1px; color: var(--on-green);
  }
  .brand-square {
    width: 18px; height: 18px; background: currentColor; display: inline-block;
  }
  .back-brand .brand-square { color: var(--on-green); }
  .services {
    font-size: 16px; line-height: 1.4; font-weight: 400;
  }

  /* Front side */
  .card--front {
    left: 625px; top: 400px;
    background: linear-gradient(180deg, var(--card-white) 0%, var(--card-white) 55%, var(--card-grey) 100%);
    color: var(--ink);
  }
  .front-brand {
    position: absolute; left: 120px; top: 52px;
    display: flex; align-items: center; gap: 12px;
    color: var(--leaf-green);
  }
  .front-brand__name {
    font-size: 44px; font-weight: 700; letter-spacing: -1.5px;
  }
  .contact-list {
    position: absolute; left: 46px; top: 136px;
    list-style: none;
    font-size: 14px; line-height: 21px; color: var(--ink);
  }
  .contact-list li { display: flex; align-items: center; gap: 8px; }
  .contact-icon { width: 12px; height: 12px; flex: none; }
  .person {
    position: absolute; right: 40px; top: 186px;
    text-align: right; font-size: 14px; line-height: 19px; color: var(--ink);
  }
  .person__name {
    color: var(--leaf-green); font-weight: 700; font-size: 19px; line-height: 24px;
  }
  .grass-strip {
    position: absolute; left: 0; right: 0; bottom: 0; height: 48px;
    background: linear-gradient(180deg, rgba(124,193,26,0) 0%, rgba(124,193,26,0.55) 45%, var(--leaf-green) 100%);
    opacity: 0.8;
  }
</style>
</head>
<body>
<main class="stage">

  <section class="card card--back" aria-label="Business card back">
    <div class="back-brand">
      <span class="brand-square" aria-hidden="true"></span>
      <span class="back-brand__name">Fernway Grove</span>
    </div>
    <p class="services">Lawn Mowing &bull; Garden Maintenance<br>Clean ups and Some Property Maintenance.</p>
  </section>

  <section class="card card--front" aria-label="Business card front">
    <div class="front-brand">
      <span class="front-brand__name">Fernway Grove</span>
      <span class="brand-square" aria-hidden="true"></span>
    </div>

    <ul class="contact-list">
      <li>
        <svg class="contact-icon" viewBox="0 0 12 12" aria-hidden="true"><path d="M2.5 1 L4.5 1 L5 3.5 L3.8 4.4 Q5 7 7.6 8.2 L8.5 7 L11 7.5 L11 9.5 Q11 11 9.5 11 Q1 10 1 2.5 Q1 1 2.5 1Z" fill="var(--leaf-green)"/></svg>
        (555) 210-4471
      </li>
      <li>
        <svg class="contact-icon" viewBox="0 0 12 12" aria-hidden="true"><rect x="2.5" y="0.5" width="7" height="11" rx="1.2" fill="none" stroke="var(--leaf-green)" stroke-width="1.4"/><rect x="4.5" y="9" width="3" height="1" fill="var(--leaf-green)"/></svg>
        (555) 318-6620
      </li>
      <li>
        <svg class="contact-icon" viewBox="0 0 12 12" aria-hidden="true"><rect x="0.5" y="2" width="11" height="8" fill="var(--leaf-green)"/><path d="M0.5 2 L6 6.5 L11.5 2" fill="none" stroke="#fff" stroke-width="1.1"/></svg>
        daniel@fernwaygrove.com
      </li>
      <li>
        <svg class="contact-icon" viewBox="0 0 12 12" aria-hidden="true"><circle cx="6" cy="6" r="5.3" fill="var(--leaf-green)"/><path d="M0.8 6 H11.2 M6 0.8 Q3 6 6 11.2 M6 0.8 Q9 6 6 11.2" fill="none" stroke="#fff" stroke-width="0.9"/></svg>
        www.fernwaygrove.com
      </li>
    </ul>

    <div class="person">
      <p class="person__name">DANIEL REYES</p>
      <p>CEO&amp;Founder</p>
      <p>412 Willowmere Road</p>
      <p>Ashford, Vermont 05101</p>
    </div>

    <div class="grass-strip" role="img" aria-label="Strip of green grass blades along the card's bottom edge"></div>
  </section>

</main>
</body>
</html>
```